Modern Skincare Product Label with Logo (please look at uploaded pics)

We need a product label and logo for a skincare line. We are looking for a design for 1 tall skinny container and 1 layout that works for short wide jar containers.

Our containers are white and silver plastic.

The dimensions of the label for the tall skinny container is about 3 1/2 in wide by 3 6/8 inches tall. That is what we want designed for.

Our product line is called Meridel Skincare. We are looking for more modern design. Please try a design with meridel in bold and going vertical down the product as well as looking at the uploaded pics we posted and getting creative with them.

We are attaching product inspirations and also our blank containers.

Target Market(s)

We are looking for something gender neutral (but slightly leaning more toward targeting women).

Industry/Entity Type

Skin Care Product

Font styles to use
Sans Serif

Colors

Designer to choose colors to be used in the design.

Requirements
Must have
• We prefer a logo and packaging that is modern, simple. The background must be white. We will have about 6 different skincare categories (categories like, acne, anti-aging, normal skin, etc). We'd like that splash of color to indicate which product category it is. accent colors: bright turquoise or Orange. can have grey and black letters. modern.
• Must have a place for a barcode, ingredients list, and any other things that we're supposed to have on a label.
Nice to have
• I'm attaching pictures we like. We are targeting more high end younger crowd.
Should not have
• No clip art or typical "spa" images or outlines of a face incorporated into the logo (we think that's super cheesy). modern and sleek design. I don't like the MS in the logo.

```html
<!DOCTYPE html>
<html lang="en">
<head>
<meta charset="utf-8">
<title>Meridel Skincare – Anti-Aging Labels</title>
<link href="https://fonts.googleapis.com/css2?family=Open+Sans:wght@400;600&family=Saira+Condensed:wght@300;400&display=swap" rel="stylesheet">
<style>
  :root {
    --turquoise: #12b9b8;
    --white: #ffffff;
    --grey-text: #5f6b6b;
    --label-edge: #d3d6d6;
    --page: #ffffff;
  }
  html, body { margin: 0; padding: 0; overflow: hidden; }
  body {
    width: 1200px;
    height: 1000px;
    background: var(--page);
    position: relative;
  }

  .label {
    position: absolute;
    box-sizing: border-box;
    border: 1px solid var(--label-edge);
    background: var(--white);
    overflow: hidden;
  }
  .label > * { position: absolute; left: 0; right: 0; margin: 0; text-align: center; }

  .header { top: 0; background: var(--turquoise); }

  .brand-name {
    font-family: "Saira Condensed", sans-serif;
    font-weight: 400;
    text-transform: uppercase;
    color: var(--turquoise);
  }
  .header + .brand-name { color: var(--white); }

  .category {
    font-family: "Saira Condensed", sans-serif;
    font-weight: 300;
    color: var(--grey-text);
  }
  .category--band { background: var(--turquoise); color: var(--white); }

  .net-weight {
    font-family: "Open Sans", sans-serif;
    color: var(--grey-text);
  }

  /* Large tall-bottle labels */
  .label--large { top: 247px; width: 193px; height: 504px; }
  .label--large .header { height: 233px; }
  .label--large .brand-name { top: 308px; font-size: 48px; line-height: 50px; top: 60px; letter-spacing: 0.5px; }
  .label--large .category { font-size: 33px; letter-spacing: 0.5px; }
  .label--large .net-weight { top: 428px; font-size: 18px; }
  .label--solid-header { left: 98px; }
  .label--solid-header .category { top: 300px; }
  .label--band { left: 316px; }
  .label--band .category--band { top: 295px; height: 53px; line-height: 53px; }

  /* Small label variants */
  .label--small { width: 115px; }
  .label--small .brand-name { font-size: 27px; line-height: 28px; }
  .label--small .category { font-size: 17px; }
  .label--small .category--band { height: 24px; line-height: 24px; }
  .label--small .net-weight { font-size: 9px; font-weight: 600; }

  .label--pump { left: 690px; top: 520px; height: 170px; }
  .label--pump .brand-name { top: 22px; }
  .label--pump .category--band { top: 98px; }
  .label--pump .net-weight { top: 150px; }

  .label--jar { left: 843px; top: 510px; height: 170px; }
  .label--jar .brand-name { top: 24px; }
  .label--jar .category--band { top: 103px; }
  .label--jar .net-weight { top: 157px; }

  .label--slim { left: 998px; top: 385px; height: 297px; }
  .label--slim .header { height: 140px; }
  .label--slim .brand-name { top: 42px; }
  .label--slim .category { top: 177px; font-size: 19px; }
  .label--slim .net-weight { top: 252px; }
</style>
</head>
<body>
  <section class="label label--large label--solid-header">
    <div class="header"></div>
    <h1 class="brand-name">Meridel<br>Skincare</h1>
    <p class="category">ANTI-AGING</p>
    <p class="net-weight">4oz (120ml)</p>
  </section>

  <section class="label label--large label--band">
    <h1 class="brand-name">Meridel<br>Skincare</h1>
    <p class="category category--band">ANTI-AGING</p>
    <p class="net-weight">4oz (120ml)</p>
  </section>

  <section class="label label--small label--pump">
    <h2 class="brand-name">Meridel<br>Skincare</h2>
    <p class="category category--band">ANTI-AGING</p>
    <p class="net-weight">2oz (60ml)</p>
  </section>

  <section class="label label--small label--jar">
    <h2 class="brand-name">Meridel<br>Skincare</h2>
    <p class="category category--band">ANTI-AGING</p>
    <p class="net-weight">2oz (60ml)</p>
  </section>

  <section class="label label--small label--slim">
    <div class="header"></div>
    <h2 class="brand-name">Meridel<br>Skincare</h2>
    <p class="category">ANTI-AGING</p>
    <p class="net-weight">4oz (120ml)</p>
  </section>
</body>
</html>
```